Logo for Internal Medicine practice

I want a logo for my Internal Medicine practice, I would like it to be with my name on it which is Lorena Valdivia Cruz.

I would like the business card to say the following (it is in Spanish since my practice is in Spanish):

Lorena Valdivia Cruz
Medicina Interna
Cel. 5587316420
lorenavaldiviacruz@correomedic.mx

Logo Text

Lorena Valdivia

```html
<!DOCTYPE html>
<html lang="es">
<head>
<meta charset="utf-8">
<title>Lorena Valdivia Cruz – Tarjeta de presentación</title>
<link rel="stylesheet" href="https://fonts.googleapis.com/css2?family=Montserrat:wght@400;500;700;800&display=swap">
<style>
  :root{
    --stage:#484848;
    --card:#141414;
    --red:#e52228;
    --blue:#3f88cf;
    --white:#f2f2f2;
    --silver:#c9c9c9;
  }
  *{margin:0;padding:0;box-sizing:border-box}
  html,body{width:1200px;height:801px;overflow:hidden}
  body{
    background:var(--stage);
    font-family:"Montserrat",sans-serif;
    display:flex;align-items:center;justify-content:center;gap:40px;
  }
  .card{
    position:relative;
    width:540px;height:310px;
    background:var(--card);
    border-radius:16px;
    border-right:3px solid var(--red);
    border-bottom:3px solid var(--red);
    overflow:hidden;
    box-shadow:0 18px 30px rgba(0,0,0,.45);
  }
  .card-tab{
    position:absolute;left:0;top:200px;
    width:14px;height:40px;
    background:var(--red);
    border-radius:0 8px 8px 0;
  }
  .contact{
    position:absolute;left:40px;top:60px;
    color:var(--white);
  }
  .contact-name{
    color:var(--red);font-weight:700;font-size:22px;letter-spacing:.2px;
  }
  .contact-role{font-size:14px;font-weight:500;margin-top:2px}
  .contact-address{font-size:13px;line-height:1.45;margin-top:18px}
  .contact-list{list-style:none;margin-top:16px;font-size:13px;line-height:1.7}
  .contact-list li{display:flex;align-items:center;gap:8px}
  .contact-list svg{width:13px;height:13px;flex:none}
  .brand{
    position:absolute;right:34px;top:118px;
    display:flex;align-items:center;gap:10px;
  }
  .brand-dot{width:18px;height:18px;border-radius:50%;background:var(--blue)}
  .brand-name{
    color:var(--red);font-weight:800;font-size:22px;letter-spacing:1px;
    text-transform:uppercase;line-height:1.05;
  }
  .card-back .brand{
    right:auto;left:50%;top:50%;transform:translate(-50%,-50%);
  }
  .card-back .brand-dot{background:var(--silver);width:24px;height:24px}
  .card-back .brand-name{color:var(--silver);font-size:30px}
</style>
</head>
<body>
  <section class="card card-front" aria-label="Anverso de la tarjeta">
    <span class="card-tab"></span>
    <div class="contact">
      <h1 class="contact-name">Lorena Valdivia Cruz</h1>
      <p class="contact-role">Medicina Interna</p>
      <p class="contact-address">3120 Avenida Los Olivos<br>Villa Serena CA 92610</p>
      <ul class="contact-list">
        <li>
          <svg viewBox="0 0 12 12" aria-hidden="true"><rect x="3" y="0.8" width="6" height="10.4" rx="1" fill="none" stroke="#e52228" stroke-width="1.3"/><circle cx="6" cy="9.4" r=".7" fill="#e52228"/></svg>
          5587316420
        </li>
        <li>
          <svg viewBox="0 0 12 12" aria-hidden="true"><rect x="0.7" y="2.3" width="10.6" height="7.4" rx="1" fill="#e52228"/><path d="M1 2.8 6 6.6 11 2.8" fill="none" stroke="#141414" stroke-width="1"/></svg>
          lorenavaldiviacruz@correomedic.mx
        </li>
        <li>
          <svg viewBox="0 0 12 12" aria-hidden="true"><circle cx="6" cy="6" r="5" fill="none" stroke="#e52228" stroke-width="1.3"/><path d="M1 6h10M6 1c-2.4 2.8-2.4 7.2 0 10M6 1c2.4 2.8 2.4 7.2 0 10" fill="none" stroke="#e52228" stroke-width="1"/></svg>
          www.lorenavaldiviacruz
        </li>
      </ul>
    </div>
    <div class="brand">
      <span class="brand-dot"></span>
      <span class="brand-name">Lorena<br>Valdivia</span>
    </div>
  </section>

  <section class="card card-back" aria-label="Reverso de la tarjeta">
    <div class="brand">
      <span class="brand-dot"></span>
      <span class="brand-name">Lorena<br>Valdivia</span>
    </div>
  </section>
</body>
</html>
```